Build Website for Playful Brand that helps content creators build businesses

Please help me create a website for my company that helps content creators build businesses around their audience. I have attached a design and vibe that I am going for at loftwren.io.

Open for changes, but I want to keep the colour I currently have (a light teal). Ultimately the brand is playful but should come off as a very modern elevated brand.

I am looking for a few pages including

1. Home (with clear CTA button)
A section where I can input what the company does, and some brands that we have launched

2. About Me
A simple page, that has preferably able to put a circular image of myself and then give a quick background about the company

3. Blog (can you include how blog posts will appear and it should sit nicely in the page)
This ideally is a section that will be able to link to another software so my blogs automatically flow into here or posts. But otherwise it should have sections of blocks where creators can see about topics that I post about

4. Contact (this should include a form that will allow users to contact me)
Finally a contact page where it links my socials, similar what is there, but ideally there is a form they can fill out which I can link to my inbox as well. This should be a simple page as well

Create a multi page website, including a page that will link or can link blog post

Similar to this vibe and logo - https://loftwren.io/

Target Market(s)

Content Creators

Coding

Coded - Design and coding required

Number of Pages Required

4 page

Requirements
Must have
• Home, Contact Me (Including a place to submit an enquiry and form), Blog Post Page As well

```html
<!DOCTYPE html>
<html lang="en">
<head>
<meta charset="utf-8">
<title>Loft Wren — Building Businesses</title>
<link rel="stylesheet" href="https://fonts.googleapis.com/css2?family=Lexend:wght@400;500;600;700&family=Poppins:wght@400;500;600&display=swap">
<style>
:root{
  --ink:#2c4448;
  --ink-deep:#243a3e;
  --teal:#7fd0c7;
  --teal-soft:#d6f1ed;
  --teal-mist:#e8f7f5;
  --stripe:#3b5256;
  --white:#ffffff;
  --muted:#5b6d70;
  --line:#c9d6d6;
}
*{box-sizing:border-box;margin:0;padding:0}
html,body{width:1200px;height:2940px;overflow:hidden}
body{position:relative;background:var(--white);font-family:"Poppins",sans-serif;color:var(--ink)}
.abs{position:absolute}
.brand-mark{display:flex;flex-direction:column;align-items:center;gap:6px}
.brand-mark .dot{width:34px;height:34px;border-radius:50%;border:3px solid var(--ink)}
.brand-mark .name{font-family:"Lexend",sans-serif;font-weight:500;font-size:17px;letter-spacing:3px;color:var(--ink)}
.btn{display:inline-flex;align-items:center;justify-content:center;background:var(--ink);color:var(--white);border-radius:30px;font-family:"Lexend",sans-serif;font-weight:600;font-size:14px;letter-spacing:1px;text-decoration:none}

/* nav */
.site-nav{top:16px;left:0;width:1200px;height:60px}
.site-nav .brand-mark{position:absolute;left:118px;top:0}
.nav-links{position:absolute;left:515px;top:20px;display:flex;gap:52px;font-family:"Lexend",sans-serif;font-size:14px;letter-spacing:1px}
.nav-links a{color:var(--ink);text-decoration:none}
.nav-links a.active{border-bottom:2px solid var(--ink);padding-bottom:4px}
.nav-cta{position:absolute;left:922px;top:10px;width:160px;height:40px;font-size:13px}

/* hero */
.hero-eyebrow{top:180px;left:112px;font-family:"Lexend",sans-serif;font-size:18px;letter-spacing:2px;color:var(--teal)}
.hero-title{top:212px;left:108px;font-family:"Lexend",sans-serif;font-weight:700;font-size:64px;line-height:68px;color:var(--ink)}
.hero-sub{top:372px;left:112px;font-size:22px;line-height:27px;font-weight:500;color:var(--ink)}
.hero-cta{top:444px;left:112px;width:170px;height:46px}
.hero-blob{top:86px;left:610px;width:420px;height:460px;border-radius:200px 200px 60px 200px;background:linear-gradient(160deg,#c9ece7,#e9f6f4 60%,#bfe5df)}

/* brands */
.brands{top:612px;left:110px;width:980px;height:226px;border-radius:24px;background:linear-gradient(180deg,var(--stripe),var(--ink-deep))}
.brands h2{position:absolute;top:52px;width:100%;text-align:center;font-family:"Lexend",sans-serif;font-weight:600;font-size:20px;letter-spacing:1px;color:var(--white)}
.brand-row{position:absolute;top:118px;left:60px;right:60px;display:flex;justify-content:space-between;align-items:center}
.brand-row span{font-family:"Lexend",sans-serif;font-weight:600;font-size:21px;color:var(--white)}

/* about */
.about-photo{top:950px;left:205px;width:350px;height:350px;border-radius:50%;background:radial-gradient(circle at 50% 40%,#eaf7f5,#c7ebe6)}
.eyebrow{font-family:"Lexend",sans-serif;font-size:16px;letter-spacing:2px;color:var(--muted)}
.section-title{font-family:"Lexend",sans-serif;font-weight:700;font-size:50px;color:var(--ink);letter-spacing:1px}
.about-copy{top:1048px;left:646px;width:440px;font-size:15.5px;line-height:21px;color:var(--ink)}
.about-copy p+p{margin-top:21px}
.about-cta{top:1284px;left:646px;width:176px;height:48px}

/* blogs */
.blogs-band{top:1470px;left:0;width:1200px;height:660px;background:linear-gradient(180deg,var(--teal-mist),#f4fbfa)}
.blog-feature{top:1662px;left:110px;width:506px;height:398px;border-radius:4px;background:linear-gradient(135deg,#9fb5b3,#5d7674 60%,#3f5557);overflow:hidden}
.blog-feature .caption{position:absolute;left:26px;bottom:26px;width:440px;color:var(--white)}
.date-tag{display:inline-block;background:var(--teal);color:var(--ink);font-size:12px;font-weight:600;padding:3px 10px;border-radius:3px}
.blog-feature .caption h3{margin-top:10px;font-family:"Lexend",sans-serif;font-weight:600;font-size:22px;line-height:28px}
.blog-card{left:626px;width:440px;height:188px;background:var(--white);border-radius:4px;display:flex;overflow:hidden;box-shadow:0 2px 8px rgba(44,68,72,.08)}
.blog-card .thumb{width:220px;height:100%;background:linear-gradient(135deg,#b6cac8,#6b8482)}
.blog-card .body{padding:18px 20px;width:220px}
.blog-card h4{margin-top:10px;font-family:"Lexend",sans-serif;font-weight:600;font-size:15px;line-height:19px}
.blog-card p{margin-top:6px;font-size:12px;line-height:16px;color:var(--muted)}
.blog-card .more{margin-top:10px;display:inline-block;border:1px solid var(--ink);font-size:10px;font-weight:600;letter-spacing:1px;padding:4px 12px;border-radius:3px}

/* contact */
.contact-panel{top:2190px;left:140px;width:946px;height:476px;background:var(--teal-soft)}
.contact-title{top:2278px;left:0;width:1200px;text-align:center}
.field{position:absolute;background:var(--white);border-radius:3px;font-size:13px;color:var(--muted);padding:14px 16px}
.send{top:2596px;left:512px;width:176px;height:50px;font-size:15px;letter-spacing:0}

/* footer */
.footer-nav{top:2800px;font-family:"Lexend",sans-serif;font-size:14px;letter-spacing:1px}
.footer-rule{height:1px;background:var(--line)}
.copyright{top:2880px;left:196px;font-size:12px;color:var(--muted)}
.follow{top:2874px;left:920px;display:flex;align-items:center;gap:10px;font-size:12px;color:var(--ink)}
.follow span.social{font-family:"Poppins",sans-serif;font-weight:600;font-size:12px}
</style>
</head>
<body>

<svg class="abs" style="top:0;left:0" width="1200" height="2940" aria-hidden="true">
  <path d="M380 940 A 220 220 0 0 1 600 1160" stroke="var(--stripe)" stroke-width="14" fill="none"/>
  <path d="M380 1380 A 220 220 0 0 1 160 1160" stroke="var(--stripe)" stroke-width="14" fill="none"/>
  <line x1="1040" y1="1000" x2="1200" y2="1000" stroke="var(--ink)" stroke-width="2"/>
  <circle cx="1040" cy="1000" r="5" fill="var(--ink)"/>
  <line x1="0" y1="1602" x2="96" y2="1602" stroke="var(--ink)" stroke-width="2"/>
  <circle cx="96" cy="1602" r="5" fill="var(--ink)"/>
</svg>

<header class="site-nav abs">
  <div class="brand-mark"><span class="dot"></span><span class="name">LOFT WREN</span></div>
  <nav class="nav-links">
    <a class="active" href="https://loftwren.io/">HOME</a>
    <a href="https://loftwren.io/">ABOUT ME</a>
    <a href="https://loftwren.io/">BLOG</a>
  </nav>
  <a class="btn nav-cta" href="https://loftwren.io/">CONTACT ME</a>
</header>

<section>
  <div class="hero-blob abs" role="img" aria-label="Smiling woman holding a tablet beside floating strategy icons"></div>
  <p class="hero-eyebrow abs">WELCOME TO LOFT WREN</p>
  <h1 class="hero-title abs">BUILDING<br>BUSINESSES</h1>
  <p class="hero-sub abs">Helping Content Creators<br>Build Their Own Brand</p>
  <a class="btn hero-cta abs" href="https://loftwren.io/">LEARN MORE</a>
</section>

<section class="brands abs">
  <h2>SUCCESSFUL BRANDS</h2>
  <div class="brand-row">
    <span>Verdanta</span><span>Alpine Ledger</span><span>Kovalt</span><span>Harbor Estates</span><span>Ashby Morrow</span>
  </div>
</section>

<section>
  <div class="about-photo abs" role="img" aria-label="Portrait of the founder smiling"></div>
  <p class="eyebrow abs" style="top:952px;left:646px">WHO WE ARE</p>
  <h2 class="section-title abs" style="top:970px;left:644px">ABOUT ME</h2>
  <div class="about-copy abs">
    <p>Lorem ipsum dolor sit amet, consectetur adipiscing elit, sed do eiusmod tempor incididunt ut labore et dolore magna aliqua. Ut enim ad minim veniam, quis nostrud exercitation ullamco laboris.</p>
    <p>Aliquip ex ea commodo consequat. Duis aute irure dolor in reprehenderit in voluptate velit esse cillum dolore eu fugiat nulla pariatur. Excepteur sint occae cat cupidatat non proident, sunt in culpa.</p>
  </div>
  <a class="btn about-cta abs" href="https://loftwren.io/">LEARN MORE</a>
</section>

<section>
  <div class="blogs-band abs"></div>
  <p class="eyebrow abs" style="top:1532px;left:110px">BLOGS &amp; RESOURCES</p>
  <h2 class="section-title abs" style="top:1556px;left:108px;font-size:46px">LATEST BLOGS</h2>
  <article class="blog-feature abs" role="img" aria-label="Team collaborating around laptops in an office">
    <div class="caption">
      <span class="date-tag">10 Jan 2024</span>
      <h3>Lorem ipsum dolor sit amet consec tetur adipiscing elit sed do</h3>
    </div>
  </article>
  <article class="blog-card abs" style="top:1662px">
    <div class="thumb" role="img" aria-label="Colleagues reviewing work on a laptop"></div>
    <div class="body">
      <span class="date-tag">14 Feb 2024</span>
      <h4>Lorem ipsum dolor sit</h4>
      <p>Sed do eiusmod tempor incididunt ut labore et dolore.</p>
      <span class="more">LEARN MORE</span>
    </div>
  </article>
  <article class="blog-card abs" style="top:1872px">
    <div class="thumb" role="img" aria-label="Creators planning content at a desk"></div>
    <div class="body">
      <span class="date-tag">22 Mar 2024</span>
      <h4>Lorem ipsum dolor sit</h4>
      <p>Ut enim ad minim veniam quis nostrud exercitation laboris.</p>
      <span class="more">LEARN MORE</span>
    </div>
  </article>
</section>

<section>
  <div class="contact-panel abs"></div>
  <div class="abs" style="top:2222px;left:582px;width:36px;height:36px;border-radius:50%;border:3px solid var(--ink)"></div>
  <h2 class="section-title contact-title abs" style="font-size:40px">CONTACT ME</h2>
  <div class="field" style="top:2344px;left:240px;width:364px;height:44px">First Name*</div>
  <div class="field" style="top:2344px;left:616px;width:364px;height:44px">Last Name*</div>
  <div class="field" style="top:2402px;left:240px;width:364px;height:44px">Email address*</div>
  <div class="field" style="top:2402px;left:616px;width:364px;height:44px">Phone*</div>
  <div class="field" style="top:2460px;left:240px;width:740px;height:118px">Leave Message</div>
  <a class="btn send abs" href="https://loftwren.io/">Send Message</a>
</section>

<footer>
  <div class="footer-rule abs" style="top:2784px;left:196px;width:340px"></div>
  <div class="footer-rule abs" style="top:2784px;left:664px;width:340px"></div>
  <div class="footer-rule abs" style="top:2838px;left:196px;width:340px"></div>
  <div class="footer-rule abs" style="top:2838px;left:664px;width:340px"></div>
  <span class="footer-nav abs" style="left:200px">HOME</span>
  <span class="footer-nav abs" style="left:340px">ABOUT US</span>
  <div class="brand-mark abs" style="top:2770px;left:538px;width:124px"><span class="dot"></span><span class="name" style="font-size:15px">LOFT WREN</span></div>
  <span class="footer-nav abs" style="left:752px">BLOGS</span>
  <span class="footer-nav abs" style="left:892px">CONTACT US</span>
  <p class="copyright abs">Copyright © 2024 Loft Wren. All Right Reserved</p>
  <div class="follow abs"><span>Follow Us:</span><span class="social">Snapnest</span><span class="social">Linkora</span></div>
</footer>

</body>
</html>
```